Infographic for law firm in criminal cases

We would like an infographic created for our law firm. We would like to highlight the information below in a more interesting, eye-catching and engaging way. There are 3 buckets of information numbered below. The numbers in bucket 1 will be updated once we receive the 2016 ones on Jan 2nd but please use these 2013 numbers as placeholders. In 2 and 3 we'd like pictures as well but very tasteful and not cartoony. Feel free to tweak text as needed but keep to the message. Since this is a law firm and serious issue, we would like the overall tone and color scheme to be appropriate as to that.

1. Total Number of DWI Arrests in Bexar County

The Marlow Parish District Attorney's Office has reported 7,649 total DWI arrests in 2013. Of the total number of arrests, 3,364 involved a blood draw. In 2013, arrests were made for the following types of DWI related offenses as follows:

5,637 arrests for a first DWI offense (including charges for a 1st DWI, open container DWI, and DWI with a BAC of .15 or greater);
1,105 arrests for a second DWI offense;
703 arrests for a third or subsequent DWI offense;
152 arrests for any DWI with a child passenger under the age of 15 years old;
37 arrests for a charge of intoxication assault;
15 arrests for intoxication manslaughter
*information obtained from the Marlow Parish District Attorney's Office

2. If you are found guilty of a DWI and you do not choose a lawyer with experience, your life can be affected with one or more of the following:
- Permanent criminal record which could impact your current and future employment.
- A driver’s license suspension from 6 months to 2 years on average.
- High fines amounts you will be required to pay based on your own case details.
- Installation of an Ignition Interlock Device system in your vehicle for an average of 1 to 3 years at your expense.
- Requirement to take DUI classes and/or counseling before any drivers license reinstatement.
- Possible requirement to pay much higher insurance rates, or lose your coverage entirely.
- Possible travel restrictions
- Community service
- Social stigma and hardships on family and friends

3. Hiring a quality criminal defense lawyer is probably the single most important decision you can make. Things to take into consideration when selecting your attorney:

- Experience. DWI law is always changing,

- Local. it's important that the attorney have experience in the city or county where the arrest took place.

- Fair fee.

Please include the law firm's name and phone number somewhere very visible and eye-catching in the infographic:

Brandt & Okafor Law
555-013-7200

We can send you their logo if it fits, it is a compass. Feel free to put something like call to speak to an experienced attorney now. The sooner you call, the sooner we can help: 555-013-7200. If you think an email is helpful their email is office@brandt-okafor.example

Possible title examples:
Former Prosecutors Fighting for You
DWI Battle? Have Prosecutors on Your Side
DWI Arrest? Fight Back

Some infographic examples that we like:

https://blog.tallyprism.example/12-infographic-tips/

We love images that show power without feeling like advertisement. Images that are thoughtful and tell a story but tasteful for example velmont's recent campaign:

https://mobile.chirpnet.example/Velmont/status/503821947716208351?ref_src=src%5Esearch%7Ccamp%5Eresults%7Cgr%5Epost

Thanks!
Dana

Industry/Entity Type

Legal

Requirements
Must have
• Must fit in 8 X 10 sheet of paper
Nice to have
• Logo. I attached word document with logo at the top. Not sure if it will fit.

```html
<!DOCTYPE html>
<html lang="en">
<head>
<meta charset="utf-8">
<title>Former Prosecutors Fighting For You</title>
<link href="https://fonts.googleapis.com/css2?family=Lato:ital,wght@0,400;0,700;0,900;1,400&display=swap" rel="stylesheet">
<style>
  :root {
    --paper: #f0eeea;
    --taupe: #9b8f88;
    --body-grey: #8c8580;
    --red: #d9434b;
    --orange: #f0953f;
    --teal: #3f8f8a;
    --teal-arrow: #4a9b96;
    --ink: #1e1b19;
    --faint: #bdb6b0;
  }
  * { margin: 0; padding: 0; box-sizing: border-box; }
  html, body { width: 960px; height: 1200px; overflow: hidden; background: var(--paper); }
  body { font-family: "Lato", sans-serif; position: relative; }
  .infographic { position: relative; width: 960px; height: 1200px; }
  .abs { position: absolute; }
  .center { left: 0; width: 960px; text-align: center; }

  .headline { top: 16px; font-size: 43px; font-weight: 900; color: var(--taupe); letter-spacing: 0.3px; }

  .marker { position: absolute; left: 0; width: 96px; height: 32px; }
  .section-lead { font-size: 19px; line-height: 24px; color: var(--body-grey); }

  .intro { top: 78px; left: 105px; width: 760px; text-align: center; }

  .total-figure { top: 182px; font-size: 40px; font-weight: 900; color: var(--red); }
  .total-label { top: 241px; font-size: 19px; color: var(--red); }
  .total-note { top: 265px; font-size: 16px; line-height: 22px; color: var(--red); }

  .stat { position: absolute; top: 334px; width: 180px; margin-left: -90px; text-align: center; color: var(--red); }
  .stat-number { font-size: 32px; font-weight: 900; line-height: 40px; }
  .stat-label { font-size: 16px; line-height: 20px; margin-top: 4px; }

  .consequences-lead { top: 487px; left: 100px; width: 760px; text-align: center; }
  .consequences { list-style: none; color: var(--orange); font-size: 16px; line-height: 20.5px; }
  .consequences li { margin-bottom: 2.5px; }
  .consequences li::before { content: "\2022\00a0"; }
  .col-left { top: 561px; left: 30px; width: 440px; }
  .col-right { top: 561px; left: 537px; width: 410px; }

  .choose-lead { top: 764px; left: 90px; width: 780px; text-align: center; }
  .tip { font-size: 16px; color: var(--teal); }
  .tip-one { top: 826px; }
  .tip-two { top: 852px; }
  .quality { top: 898px; font-size: 24px; font-weight: 700; color: var(--teal); }
  .quality-left { left: 50px; }
  .quality-mid { left: 0; width: 960px; text-align: center; }
  .quality-right { right: 49px; }

  .phone { top: 976px; font-size: 36px; font-weight: 900; color: var(--taupe); }

  .firm { top: 1090px; left: 0; width: 960px; display: flex; justify-content: center; align-items: center; gap: 18px; }
  .firm-mark { width: 70px; height: 70px; border: 3px solid var(--ink); border-radius: 50%; }
  .firm-name { font-size: 40px; font-weight: 400; color: var(--ink); letter-spacing: 1px; }

  .source { right: 6px; bottom: 3px; font-size: 11px; font-style: italic; color: var(--faint); }
</style>
</head>
<body>
<main class="infographic">
  <h1 class="abs center headline">FORMER PROSECUTORS FIGHTING FOR YOU</h1>

  <svg class="marker" style="top:82px" viewBox="0 0 96 32" aria-hidden="true"><polygon points="0,0 76,0 96,16 76,32 0,32" fill="var(--red)"/></svg>
  <p class="abs section-lead intro">The Marlow Parish District Attorney's Office has reported 7,649 total DWI arrests in 2013. Of the total number of arrests, 3,364 involved a blood draw. In 2013, arrests were made for the following types of DWI related offenses as follows:</p>

  <div class="abs center total-figure">5,637</div>
  <div class="abs center total-label">Arrests for a first DWI offense</div>
  <div class="abs center total-note">(including charges for a 1st DWI, open container<br>DWI, and DWI with a BAC of .15 or greater)</div>

  <div class="stat" style="left:76px"><div class="stat-number">1,105</div><div class="stat-label">arrests for a<br>second DWI<br>offense</div></div>
  <div class="stat" style="left:277px"><div class="stat-number">703</div><div class="stat-label">arrests for a third<br>or subsequent<br>DWI offense</div></div>
  <div class="stat" style="left:478px"><div class="stat-number">152</div><div class="stat-label">arrests for any<br>DWI with a child<br>passenger under the<br>age of 15 years old</div></div>
  <div class="stat" style="left:678px"><div class="stat-number">37</div><div class="stat-label">arrests for<br>a charge of<br>intoxication assault</div></div>
  <div class="stat" style="left:879px"><div class="stat-number">15</div><div class="stat-label">arrests for<br>intoxication<br>manslaughter</div></div>

  <svg class="marker" style="top:491px" viewBox="0 0 96 32" aria-hidden="true"><polygon points="0,0 76,0 96,16 76,32 0,32" fill="var(--orange)"/></svg>
  <p class="abs section-lead consequences-lead">If you are found guilty of a DWI and you do not choose a lawyer with experience, your life can be affected with one or more of the following:</p>

  <ul class="abs consequences col-left">
    <li>Permanent criminal record which could impact your current and future employment.</li>
    <li>A driver’s license suspension from 6 months to 2 years on average.</li>
    <li>High fines amounts you will be required to pay based on your own case details.</li>
    <li>Installation of an Ignition Interlock Device system in your vehicle for an average of 1-3 years at your expense.</li>
  </ul>
  <ul class="abs consequences col-right">
    <li>Requirement to take DUI classes and/or counseling before any drivers license reinstatement.</li>
    <li>Possible requirement to pay much higher insurance rates, or lose your coverage entirely.</li>
    <li>Possible travel restrictions</li>
    <li>Community service</li>
    <li>Social stigma and hardships on family and friends</li>
  </ul>

  <svg class="marker" style="top:766px" viewBox="0 0 96 32" aria-hidden="true"><polygon points="0,0 76,0 96,16 76,32 0,32" fill="var(--teal-arrow)"/></svg>
  <p class="abs section-lead choose-lead">Hiring a quality criminal defense lawyer is probably the single most important decision that you can make. Things to take into consideration when selecting your attorney:</p>

  <div class="abs center tip tip-one">DWI law is always changing</div>
  <div class="abs center tip tip-two">Your attorney understands the city or county where the arrest took place</div>

  <div class="abs quality quality-left">Experienced</div>
  <div class="abs quality quality-mid">Local</div>
  <div class="abs quality quality-right">Fair Fee</div>

  <div class="abs center phone">555-013-7200</div>

  <div class="abs firm">
    <span class="firm-mark" aria-hidden="true"></span>
    <span class="firm-name">BRANDT &amp; OKAFOR</span>
  </div>

  <div class="abs source">*information obtained from the Marlow Parish District Attorney's Office</div>
</main>
</body>
</html>
```